Spanish Student Needs a Cover for his PhD Dissertation

Hi everyone :) So, I'm a Corneal surgeon currently finishing my PhD, with a dissertation focused on the evaluation of quality of life in patients affected by a disease called Keratoconus. Just so you know, Keratoconus is a condition in which the cornea (the frontal part of the way) gets thin and bulgy and it decreases vision. What I did during my PhD was designing a questionnaire for evaluating quality of life in this kind of patients.
I need to design a hard cover for my dissertation, which is 200 sheets long. I like kind of minimalistic and geometric designs but I am totally open to suggestions. What needs to be in the cover is the name of the dissertation "Diseño, desarrollo y validación de una encuesta para evaluar el compromiso visual y emocional subjetivos en pacientes con Queratocono" and my name, "Iñigo Tarrasco". The other thing that needs to go there is the logo of my university (Universidad de Montebrisa). Aside from that, anything else is up to the designer. It would be important to use the kind of "red" color I am using in the dissertation. I am attaching the frontal page of my dissertation so you know what kind of design and colors I am using.
In the back part, of the cover, there should be this small inscription: "Iñigo Tarrasco, MD, es un Oftalmólogo Subespecialista en Cirugía Refractiva de la Universidad Serrana Metropolitana (Colombia) y la Universidad de Montebrisa (España). Actualmente se desempeña como miembro del Departamento de Córnea y Cirugía Refractiva de la Clínica de Oftalmología Vallealto y como director de su propia compañía de emprendimiento médico Silver Heron Surgical". Please leave a space to place my picture; I will have it taken this week so I don't have it right now, you can just leave the blank spot and I will include it later
The size of the pages is standard "letter" size.
Thanks a lot!

Target Market(s)

PhD Scholars

Font styles to use
Serif

Requirements
Must have
• The "red" color I use on my font. It must be formal but "young".
Nice to have
• I like to keep the design clean, kind of "formal with a young" touch so to speak. I really like gray colors, so it would be nice to have broad areas of gray. I love geometrical designs.
I have uploaded a very early version a friend of mine made (it even had a different title); this can be a starting point for you to work on, but I am more than open to suggestions and new ideas.
Should not have
• Please don't use my whole name, Iñigo Tarrasco is fine. I don't like ALL CAPITALS.

```html
<!DOCTYPE html>
<html lang="es">
<head>
<meta charset="utf-8">
<title>Cubierta de tesis doctoral – Iñigo Tarrasco</title>
<link href="https://fonts.googleapis.com/css2?family=Libre+Caslon+Text:wght@400;700&family=Noto+Serif:wght@700&family=Poppins:wght@600&family=Roboto:wght@500;700&display=swap" rel="stylesheet">
<style>
  :root {
    --paper: #ffffff;
    --charcoal: #262626;
    --crimson: #a81c40;
    --accent-red: #e4432f;
    --ink: #1d1d1d;
    --rule: #8c8c8c;
    --photo-warm: #c9773a;
    --photo-amber: #b88b2c;
    --photo-rose: #e6c9c4;
  }
  * { box-sizing: border-box; margin: 0; padding: 0; }
  html, body {
    width: 1200px; height: 930px; overflow: hidden;
    background: var(--paper);
  }
  .sheet { position: relative; width: 1200px; height: 930px; }

  .side-label {
    position: absolute; width: 200px; text-align: center;
    font-family: "Libre Caslon Text", serif; font-size: 20px;
    color: var(--crimson);
  }
  .side-label--front { left: 220px; top: 52px; }
  .side-label--back  { left: 804px; top: 58px; }

  .cover {
    position: absolute; top: 113px; width: 535px; height: 693px;
    background: var(--charcoal);
    box-shadow: 6px 8px 10px rgba(0,0,0,.55);
    overflow: hidden;
  }
  .cover--front { left: 54px; }
  .cover--back  { left: 612px; }

  .cover__art { position: absolute; inset: 0; }

  .university {
    position: absolute; left: 13px; top: 16px; width: 128px;
    text-align: center;
  }
  .university__seal {
    width: 51px; height: 51px; margin: 0 auto;
    border-radius: 50%; background: var(--paper);
  }
  .university__rule {
    height: 1px; background: var(--rule); margin-top: 9px;
  }
  .university__name {
    margin-top: 5px;
    font-family: "Roboto", sans-serif; font-weight: 700;
    font-size: 10.2px; color: var(--paper); white-space: nowrap;
  }
  .doctoral-school {
    margin: 6px auto 0; width: 125px; height: 31px;
    padding: 0 4px;
    background: var(--paper);
    display: flex; align-items: center; justify-content: center;
    text-align: center;
    font-family: "Roboto", sans-serif; font-weight: 500;
    font-size: 8.5px; line-height: 10.5px; color: var(--ink);
  }

  .thesis-title {
    position: absolute; left: 15px; top: 186px; width: 360px;
    font-family: "Noto Serif", serif; font-weight: 700;
    font-size: 21.6px; line-height: 29.5px; letter-spacing: .7px;
    color: var(--paper); white-space: nowrap;
  }
  .author-name {
    position: absolute; left: 14px; top: 416px;
    font-family: "Poppins", sans-serif; font-weight: 600;
    font-size: 23px; letter-spacing: 2.3px;
    color: var(--paper);
  }

  .author-bio {
    position: absolute; left: 100px; top: 40px; width: 335px;
    text-align: center;
    font-family: "Libre Caslon Text", serif;
    font-size: 15.6px; line-height: 18.9px;
    color: var(--paper);
  }
  .author-photo-slot {
    position: absolute; left: 150px; top: 278px;
    width: 234px; height: 314px; border-radius: 22px;
    background: var(--paper);
    display: flex; align-items: center; justify-content: center;
    font-family: "Libre Caslon Text", serif; font-size: 15px;
    color: var(--ink);
  }
</style>
</head>
<body>
<main class="sheet">
  <p class="side-label side-label--front">Front</p>
  <p class="side-label side-label--back">Back</p>

  <section class="cover cover--front">
    <svg class="cover__art" width="535" height="693" viewBox="0 0 535 693">
      <defs>
        <linearGradient id="eye-tones" x1="1" y1="0" x2="0" y2="1">
          <stop offset="0" stop-color="var(--photo-rose)"/>
          <stop offset=".3" stop-color="var(--photo-warm)"/>
          <stop offset=".65" stop-color="var(--photo-amber)"/>
          <stop offset="1" stop-color="var(--photo-rose)"/>
        </linearGradient>
      </defs>
      <polygon role="img" aria-label="Fotografía en primer plano de un ojo con iris ámbar y pestañas"
               points="535,59 535,693 123,693" fill="url(#eye-tones)"/>
      <polygon class="title-band" points="0,167 482,167 325,386 0,386" fill="var(--crimson)"/>
      <polygon class="title-band__accent" points="482,167 509,207 453,207" fill="var(--accent-red)"/>
    </svg>

    <div class="university">
      <div class="university__seal"></div>
      <div class="university__rule"></div>
      <p class="university__name">Universidad de Montebrisa</p>
      <p class="doctoral-school">Escuela de Doctorado<br>de Montebrisa</p>
    </div>

    <h1 class="thesis-title">"Diseño, desarrollo y<br>validación de una encuesta<br>para evaluar el compromiso<br>visual y emocional<br>subjetivos en pacientes con<br>Queratocono"</h1>
    <p class="author-name">Iñigo Tarrasco</p>
  </section>

  <section class="cover cover--back">
    <p class="author-bio">"Iñigo Tarrasco, MD, es un Oftalmólogo Subespecialista en Cirugía Refractiva de la Universidad Serrana Metropolitana (Colombia) y la Universidad de Montebrisa (España). Actualmente se desempeña como miembro del Departamento de Córnea y Cirugía Refractiva de la Clínica de Oftalmología Vallealto y como director de su propia compañía de emprendimiento médico Silver Heron Surgical"</p>
    <div class="author-photo-slot">Author Photo here</div>
  </section>
</main>
</body>
</html>
```